Design a sharp Business Card, Stationary, and PowerPoint Template for Harbor Lantern Group (HLG)
Harbor Lantern Group (HLG) is a consulting firm with a mission
Professional
Maren Coleby Ashdown
Managing Director
4870 Larkspur Blvd. NW
Suite 2300
Washington, DC 20417
maren@harborlntn.example
www.harborlntn.example
I'm looking for something sharp that incorporates the colors of the logo.
Business card designs (only), please include this text:
We work with the military, private sector, and nonprofits to protect people affected by conflict and disaster.
This is the logo for Harbor Lantern Group (HLG). The black and red color combo is preferred.
For design purposes, the symbol can be used separately from the text and watermarked.

```html
<!DOCTYPE html>
<html lang="en">
<head>
<meta charset="utf-8">
<title>Harbor Lantern Group — Business Card</title>
<link rel="stylesheet" href="https://fonts.googleapis.com/css2?family=Montserrat:wght@300;400;600;700&family=Open+Sans:wght@400;600&display=swap">
<style>
  :root {
    --canvas: #e9e7e4;
    --card-dark: #2a2a2c;
    --card-light: #ffffff;
    --accent-red: #c8102e;
    --text-dark: #2a2a2c;
    --text-light: #ffffff;
    --text-muted: #bdbdbd;
    --rule-grey: #d9d9d9;
  }
  * { box-sizing: border-box; margin: 0; padding: 0; }
  html, body { width: 1200px; height: 629px; overflow: hidden; }
  body {
    background: var(--canvas);
    font-family: "Open Sans", Arial, sans-serif;
    position: relative;
  }
  .card {
    position: absolute;
    top: 166px;
    width: 520px;
    height: 297px;
    border-radius: 3px;
    overflow: hidden;
    box-shadow: 0 6px 18px rgba(0,0,0,0.18);
  }
  /* Back of card */
  .card-back { left: 50px; background: var(--card-dark); color: var(--text-light); text-align: center; }
  .back-mark {
    margin: 74px auto 0;
    display: flex; flex-direction: column; align-items: center; gap: 10px;
  }
  .mark-dot { width: 34px; height: 34px; border-radius: 50%; background: var(--accent-red); }
  .back-name {
    font-family: "Montserrat", Arial, sans-serif; font-weight: 300;
    font-size: 15px; letter-spacing: 4px; text-transform: uppercase;
  }
  .back-intro { margin-top: 26px; font-size: 8px; color: var(--text-muted); letter-spacing: 0.5px; }
  .back-sectors {
    margin-top: 4px;
    font-family: "Montserrat", Arial, sans-serif; font-weight: 700;
    font-size: 11px; letter-spacing: 0.6px;
  }
  .back-mission { margin-top: 4px; font-size: 8px; color: var(--text-muted); padding: 0 90px; line-height: 1.4; }

  /* Front of card */
  .card-front { left: 630px; background: var(--card-light); }
  .front-wave { position: absolute; left: 0; top: 0; width: 520px; height: 297px; }
  .front-brand {
    position: absolute; left: 188px; top: 44px;
    display: flex; align-items: center; gap: 16px;
  }
  .front-brand .mark-dot { width: 48px; height: 48px; }
  .front-name {
    font-family: "Montserrat", Arial, sans-serif; font-weight: 300;
    font-size: 20px; letter-spacing: 5px; line-height: 1.25;
    text-transform: uppercase; color: var(--text-dark);
  }
  .person { position: absolute; left: 32px; top: 186px; color: var(--text-light); }
  .person-name { color: var(--accent-red); font-weight: 600; font-size: 13px; font-family: "Montserrat", Arial, sans-serif; }
  .person-title { font-size: 9px; margin-top: 2px; color: var(--text-muted); }
  .person-address { font-size: 9px; margin-top: 12px; line-height: 1.45; }
  .contacts { position: absolute; left: 322px; top: 180px; list-style: none; color: var(--text-light); }
  .contact { display: flex; align-items: center; gap: 8px; font-size: 9px; height: 17px; }
  .contact-icon { width: 12px; height: 12px; flex: none; }
</style>
</head>
<body>

<section class="card card-back" aria-label="Business card back">
  <div class="back-mark">
    <span class="mark-dot"></span>
    <span class="back-name">Harbor Lantern Group</span>
  </div>
  <p class="back-intro">We work with the</p>
  <p class="back-sectors">MILITARY | PRIVATE SECTOR | NONPROFITS</p>
  <p class="back-mission">to protect people affected by conflict and disaster.</p>
</section>

<section class="card card-front" aria-label="Business card front">
  <svg class="front-wave" viewBox="0 0 520 297" aria-hidden="true">
    <path d="M0 150 C150 205 330 190 520 120 L520 297 L0 297 Z" fill="#2a2a2c"/>
    <path d="M0 160 C160 212 330 195 520 132 L520 142 C330 205 160 222 0 170 Z" fill="#ffffff"/>
    <path d="M0 150 C150 200 330 186 520 118 L520 124 C330 193 150 207 0 156 Z" fill="#c8102e"/>
  </svg>

  <div class="front-brand">
    <span class="mark-dot"></span>
    <span class="front-name">Harbor<br>Lantern<br>Group</span>
  </div>

  <div class="person">
    <p class="person-name">Maren Coleby Ashdown</p>
    <p class="person-title">Managing Director</p>
    <p class="person-address">4870 Larkspur Blvd. NW<br>Suite 2300, Washington, DC 20417</p>
  </div>

  <ul class="contacts">
    <li class="contact">
      <svg class="contact-icon" viewBox="0 0 12 12"><circle cx="6" cy="6" r="6" fill="#c8102e"/><path d="M4 3.2l1 1.4-.6.7c.4.9 1 1.5 1.9 1.9l.7-.6 1.4 1-.5 1c-2.3-.2-4-1.9-4.3-4.3z" fill="#fff"/></svg>
      202.555.0148
    </li>
    <li class="contact">
      <svg class="contact-icon" viewBox="0 0 12 12"><circle cx="6" cy="6" r="6" fill="#c8102e"/><rect x="4.2" y="2.8" width="3.6" height="6.4" rx="0.6" fill="#fff"/></svg>
      202.555.0193
    </li>
    <li class="contact">
      <svg class="contact-icon" viewBox="0 0 12 12"><circle cx="6" cy="6" r="6" fill="#c8102e"/><rect x="3" y="4" width="6" height="4.2" fill="#fff"/><path d="M3 4l3 2.3L9 4" stroke="#c8102e" stroke-width="0.7" fill="none"/></svg>
      maren@harborlntn.example
    </li>
    <li class="contact">
      <svg class="contact-icon" viewBox="0 0 12 12"><circle cx="6" cy="6" r="6" fill="#c8102e"/><circle cx="6" cy="6" r="2.8" stroke="#fff" stroke-width="0.8" fill="none"/><path d="M3.2 6h5.6M6 3.2v5.6" stroke="#fff" stroke-width="0.6"/></svg>
      www.harborlntn.example
    </li>
    <li class="contact">
      <svg class="contact-icon" viewBox="0 0 12 12"><circle cx="6" cy="6" r="6" fill="#c8102e"/><circle cx="6" cy="6" r="2" fill="#fff"/></svg>
      @mashdown
    </li>
  </ul>
</section>

</body>
</html>
```